Brightway Haul & Repair Services, are a company that offers a 'one stop shop' pre-move clean up a

I have already selected a logo which I would like on the front of the business cards along with phone numbers, web address and email which are:
0419574302
www.brightwayhaul.com.au
brightwayhaulrepair@mailbox.example

On the back of the card I would like to list some of the types of service we offer (clean - move - repairs/maintenance) which are:
CLEAN - windows, gutters, solar panels, driveways/paths, carpets.
MOVE - Small/medium size house/office moves, large item pick-up & delivery, yard clean-up and removal.
General maintenance and repairs.

I would like the blue logo on a gray background.

Thanks

```html
<!DOCTYPE html>
<html lang="en">
<head>
<meta charset="utf-8">
<title>Brightway Haul &amp; Repair Services – Business Cards</title>
<link rel="stylesheet" href="https://fonts.googleapis.com/css2?family=Roboto+Condensed:wght@700&family=Arimo:wght@400&display=swap">
<style>
  :root {
    --paper: #ffffff;
    --edge: #333333;
    --brand-blue: #1a77c2;
    --band-blue: #0a8ddf;
    --band-dark: #1e1a19;
    --band-grey: #d9d9d9;
    --text-dark: #1a1a1a;
    --text-grey: #6b6b6b;
    --accent: #1a8ad4;
    --white: #ffffff;
  }
  * { margin: 0; padding: 0; box-sizing: border-box; }
  html, body {
    width: 1200px; height: 750px; overflow: hidden;
    background: var(--paper);
  }
  .sheet { position: relative; width: 1200px; height: 750px; }

  .card {
    position: absolute;
    background: var(--paper);
    border: 1px solid var(--edge);
    overflow: hidden;
  }
  .card--front-wide { left: 41px; top: 108px; width: 459px; height: 282px; }
  .card--back-wide  { left: 41px; top: 447px; width: 459px; height: 282px; }
  .card--front-tall { left: 552px; top: 178px; width: 283px; height: 459px; }
  .card--back-tall  { left: 865px; top: 178px; width: 283px; height: 459px; }

  .brand {
    position: absolute;
    font-family: "Roboto Condensed", "Arial Narrow", sans-serif;
    font-weight: 700;
    color: var(--brand-blue);
    text-align: center;
    text-transform: uppercase;
    line-height: 1;
    white-space: nowrap;
  }
  .brand__main, .brand__sub { display: block; }

  .brand--large { width: 300px; }
  .brand--large .brand__main { font-size: 38px; letter-spacing: 0.3px; }
  .brand--large .brand__sub  { font-size: 17px; margin-top: 8px; letter-spacing: 0.3px; }

  .brand--medium { width: 300px; }
  .brand--medium .brand__main { font-size: 33px; }
  .brand--medium .brand__sub  { font-size: 15px; margin-top: 7px; }

  .brand--small { width: 150px; }
  .brand--small .brand__main { font-size: 20px; }
  .brand--small .brand__sub  { font-size: 9px; margin-top: 4px; }

  .card--front-wide .brand { left: 117px; top: 98px; }
  .card--front-tall .brand { left: -8px; top: 178px; }
  .card--back-wide .brand  { left: 297px; top: 50px; }
  .card--back-tall .brand  { left: 25px; top: 56px; }

  .wave { position: absolute; left: 0; top: 0; width: 459px; height: 282px; }

  .contact {
    position: absolute;
    font-family: "Roboto Condensed", "Arial Narrow", sans-serif;
    font-weight: 700;
    color: var(--white);
    list-style: none;
    white-space: nowrap;
  }
  .card--front-wide .contact { left: 28px; top: 212px; font-size: 16px; line-height: 20px; }
  .contact__item { display: flex; align-items: center; gap: 10px; }
  .contact__icon { width: 14px; height: 14px; flex: none; }

  .band-grey { position: absolute; left: 0; top: 359px; width: 100%; height: 8px; background: var(--band-grey); }
  .band-blue { position: absolute; left: 0; top: 367px; width: 100%; height: 92px; background: var(--band-blue); }
  .card--front-tall .contact { left: 12px; top: 387px; font-size: 13.5px; line-height: 16.5px; }

  .services {
    position: absolute;
    font-family: Arimo, Arial, sans-serif;
    color: var(--text-grey);
    white-space: nowrap;
  }
  .services__title { color: var(--text-dark); font-size: 17px; font-weight: 400; line-height: 20px; margin-bottom: 12px; }
  .services__list { list-style: none; margin-left: 4px; font-size: 13.5px; line-height: 17.8px; }
  .services__group { margin-bottom: 17px; }
  .services__head { display: block; text-transform: uppercase; }

  .card--back-wide .services { left: 21px; top: 42px; }
  .card--back-tall .services { left: 26px; top: 207px; }
  .card--back-tall .services__head { color: var(--accent); }
</style>
</head>
<body>
<main class="sheet">

  <section class="card card--front-wide">
    <svg class="wave" viewBox="0 0 459 282" aria-hidden="true">
      <path d="M0 178 C110 172 250 215 459 262 L459 282 L0 282 Z" fill="var(--band-blue)"/>
      <path d="M0 174 C110 166 250 200 459 244 L459 262 C250 215 110 172 0 178 Z" fill="var(--band-dark)"/>
    </svg>
    <div class="brand brand--large">
      <span class="brand__main">Brightway Haul</span>
      <span class="brand__sub">&amp; Repair Services</span>
    </div>
    <ul class="contact">
      <li class="contact__item">
        <svg class="contact__icon" viewBox="0 0 14 14" aria-hidden="true">
          <circle cx="7" cy="7" r="6.2" fill="none" stroke="#fff" stroke-width="1.2"/>
          <path d="M4.6 3.8 L5.8 3.6 L6.4 5.4 L5.6 6 C6 7 7 8 8 8.4 L8.6 7.6 L10.4 8.2 L10.2 9.4 C7 9.6 4.4 7 4.6 3.8 Z" fill="#fff"/>
        </svg>
        <span>0419574302</span>
      </li>
      <li class="contact__item">
        <svg class="contact__icon" viewBox="0 0 14 14" aria-hidden="true">
          <circle cx="7" cy="7" r="5.5" fill="#9fd3f5" stroke="#fff" stroke-width="1"/>
          <path d="M1.5 7 H12.5 M7 1.5 V12.5" stroke="#fff" stroke-width="0.8"/>
        </svg>
        <span>www.brightwayhaul.com.au</span>
      </li>
      <li class="contact__item">
        <svg class="contact__icon" viewBox="0 0 14 14" aria-hidden="true">
          <circle cx="7" cy="7" r="5.5" fill="#9fd3f5" stroke="#fff" stroke-width="1"/>
          <path d="M4 5 H10 V9.5 H4 Z M4 5 L7 7.4 L10 5" fill="none" stroke="#fff" stroke-width="0.8"/>
        </svg>
        <span>brightwayhaulrepair@mailbox.example</span>
      </li>
    </ul>
  </section>

  <section class="card card--back-wide">
    <div class="services">
      <h2 class="services__title">Service we offer :</h2>
      <ul class="services__list">
        <li class="services__group"><span class="services__head">Clean</span>Windows, Gutters, Solar Panels,<br>Driveways/Paths, Carpets.</li>
        <li class="services__group"><span class="services__head">Move</span>Small/medium size House/Office Moves,<br>Large Item Pick-up &amp; Delivery,<br>Yard Clean-Up and Removal.</li>
        <li>General maintenance and repairs.</li>
      </ul>
    </div>
    <div class="brand brand--small">
      <span class="brand__main">Brightway Haul</span>
      <span class="brand__sub">&amp; Repair Services</span>
    </div>
  </section>

  <section class="card card--front-tall">
    <div class="brand brand--medium">
      <span class="brand__main">Brightway Haul</span>
      <span class="brand__sub">&amp; Repair Services</span>
    </div>
    <div class="band-grey"></div>
    <div class="band-blue"></div>
    <ul class="contact">
      <li>0419574302</li>
      <li>www.brightwayhaul.com.au</li>
      <li>brightwayhaulrepair@mailbox.example</li>
    </ul>
  </section>

  <section class="card card--back-tall">
    <div class="brand brand--small">
      <span class="brand__main">Brightway Haul</span>
      <span class="brand__sub">&amp; Repair Services</span>
    </div>
    <div class="services">
      <h2 class="services__title">Service we offer :</h2>
      <ul class="services__list">
        <li class="services__group"><span class="services__head">Clean</span>Windows, Gutters, Solar Panels,<br>Driveways/Paths, Carpets.</li>
        <li class="services__group"><span class="services__head">Move</span>Small/medium size House/Office Moves,<br>Large Item Pick-up &amp; Delivery,<br>Yard Clean-Up and Removal.</li>
        <li>General maintenance and repairs.</li>
      </ul>
    </div>
  </section>

</main>
</body>
</html>
```